Webdesign für Gerüstbau Brenner
Zielgruppe
In der über 20-jährigen erfolgreichen Firmengeschichte ist die Firma Gerüstbau Brenner GmbH ein leistungsstarker und kompetenter Partner für Kunden im Raum Sachsen und Thüringen. Der Aktionsradius erstreckt sich auf ca. 100 km um die Stadt Glauchau OT Niederschindmaas herum. Das Unternehmen arbeitet ausschließlich mit Kolvex-Gerüsten.
Dafür stehen ca. 40.000 m² Kolvex-Sturm-Gerüst, ca. 4.000 m² Modulgerüst, Kassetten- und Planendächer, Treppenaufgänge und Nottreppen, Fahr- und Rollgerüste sowie weitere Sonderteile zur Verfügung.
Zielgruppe sind:
- Bau- und Dachdeckerfirmen,
- Handwerksbetriebe,
- Ingenieurbüros,
- Kommunen,
- Kirchen,
- landwirtschaftlichen Betriebe,
- Industrie
- und Privatpersonen
Aufgabenstellung
Unserem Auftraggeber gefällt ein großes Auftaktfoto gut, ansonsten ist er offen für ein modernes Layout.
- Layout als PSD
- Notwendige Bilder ausschließlich von Bildquell-Archiv.de
- Bitte nur die Startseite layouten
- blau des Logos und eine Zweitfarbe
- Slogan: Wir lösen Ihre Gerüstprobleme! Sprechen Sie mit uns!

```html
<!DOCTYPE html>
<html lang="de">
<head>
<meta charset="utf-8">
<title>Gerüstbau Brenner – Startseite</title>
<link href="https://fonts.googleapis.com/css2?family=Roboto:wght@300;400;500;700;900&family=Poppins:wght@400;600;700&display=swap" rel="stylesheet">
<style>
:root{
  --blue:#0d5a90;
  --blue-dark:#0a4a78;
  --green:#76b82a;
  --text:#555;
  --heading:#2b2b2b;
  --footer:#2d2d2d;
  --light:#f4f6f8;
}
*{box-sizing:border-box;margin:0;padding:0}
html,body{width:1200px;height:2457px;overflow:hidden;background:#fff}
body{font-family:"Roboto",sans-serif;color:var(--text);position:relative}
.wrap{width:732px;margin:0 auto;position:relative;height:100%}

/* header */
.site-header{height:100px;position:relative;background:#fff;z-index:5}
.brand{position:absolute;left:0;top:15px;display:flex;align-items:center;gap:12px}
.brand-square{width:71px;height:71px;background:var(--blue)}
.brand-name{font-size:21px;color:var(--blue);font-weight:400;line-height:1.05}
.brand-name small{display:block;font-size:12px}
.main-nav{position:absolute;left:194px;top:53px;display:flex;gap:30px;font-size:10.5px;color:#444;white-space:nowrap}
.main-nav .active{color:var(--green)}
.dropdown{position:absolute;left:268px;top:75px;width:176px;background:#f3f3f3;box-shadow:0 2px 6px rgba(0,0,0,.15);z-index:5;font-size:10px;color:#444}
.dropdown li{list-style:none;padding:11px 19px;border-bottom:1px solid #e0e0e0;line-height:1.25}
.dropdown li:first-child{color:var(--green)}
.dropdown li:last-child{border-bottom:none}

/* hero */
.hero{height:419px;position:relative;background:linear-gradient(180deg,#6f8fb8 0%,#b9c8dc 40%,#d9dde4 60%,#3b3a40 85%,#241f22 100%)}
.hero-cta{position:absolute;left:725px;top:137px;width:240px;height:143px;background:#fff;padding:20px 12px 20px 21px}
.hero-cta h1{font-family:"Poppins",sans-serif;font-weight:400;font-size:18.5px;line-height:1.25;color:var(--heading);white-space:nowrap}
.hero-cta h1 b{color:var(--blue);font-weight:700}
.hero-cta p{font-family:"Poppins",sans-serif;font-size:11px;margin-top:8px;color:#333}
.phone-pill{display:inline-flex;align-items:center;gap:6px;margin-top:12px;background:var(--green);color:#fff;border-radius:11px;font-size:7.5px;font-weight:700;padding:4px 4px 4px 9px}
.phone-pill span{width:14px;height:14px;border-radius:50%;background:#fff;display:inline-block}

/* about */
.about{height:450px;position:relative}
.badge{display:inline-block;color:#fff;font-weight:700;font-size:17px;padding:6px 13px;position:relative}
.badge::after{content:"";position:absolute;left:0;bottom:-7px;border-left:8px solid var(--blue);border-bottom:7px solid transparent}
.badge.blue{background:var(--blue)}
.badge.green{background:var(--green)}
.badge.green::after{border-left-color:var(--green)}
.about .badge{position:absolute;left:0;top:50px;z-index:2}
.about h2{position:absolute;left:0;top:100px;font-size:22px;font-weight:700;color:var(--heading);line-height:1.1;white-space:nowrap;z-index:2}
.about h2 em{font-style:normal;color:var(--green)}
.about h2 span{display:block;font-weight:400;padding-left:60px}
.about-text{position:absolute;left:2px;top:170px;width:345px;font-size:9.5px;line-height:18.7px;z-index:2}
.btn-outline{position:absolute;left:1px;top:376px;width:106px;height:31px;border:2px solid var(--blue);border-radius:16px;color:var(--blue);font-size:10px;font-weight:700;display:flex;align-items:center;justify-content:center;z-index:2}
.about-visual{position:absolute;left:370px;top:53px;width:444px;height:353px;background:radial-gradient(ellipse at 50% 60%,#e9edf1 0%,#fff 70%);z-index:1}

/* services */
.services{height:687px;background:var(--blue);position:relative;text-align:center;color:#fff}
.services .badge{margin-top:53px}
.services .badge::after{display:none}
.services-intro{font-size:9.6px;line-height:18.7px;margin-top:22px}
.slider{position:absolute;left:0;top:252px;width:732px;display:flex;gap:19px}
.svc-card{width:231px;height:308px;background:#fff}
.svc-card .photo{height:251px}
.svc-card h3{font-size:11.5px;font-weight:500;color:#333;line-height:57px}
.arrow{position:absolute;top:374px}
.dots{position:absolute;left:0;right:0;top:606px;display:flex;justify-content:center;gap:7px}
.dots i{width:6px;height:6px;border-radius:50%;background:var(--green)}
.dots i:first-child{background:#fff}
.services-band{position:absolute;left:0;right:0;bottom:0;height:32px;background:var(--blue-dark);opacity:.5}

/* news */
.news{height:523px;text-align:center;position:relative}
.news .badge{margin-top:57px}
.news .badge::after{display:none}
.news-grid{position:absolute;left:0;top:124px;display:flex;gap:19px;text-align:left}
.news-card{width:231px;height:325px;background:#fff;box-shadow:0 1px 6px rgba(0,0,0,.12)}
.news-card .photo{height:134px}
.news-card .body{padding:16px 18px}
.news-card h3{font-size:11.5px;font-weight:500;color:#222;line-height:15px;margin-top:2px}
.news-card p{font-size:9.4px;line-height:15.6px;margin-top:13px;color:#666}
.news-card a{display:block;font-size:9.5px;font-weight:700;color:var(--blue);margin-top:11px;text-decoration:none}

/* footer */
.site-footer{height:224px;background:var(--footer);color:#ddd;position:relative}
.site-footer h4{font-size:11.5px;font-weight:700;color:#fff;position:absolute;top:44px}
.foot-links{position:absolute;left:6px;top:77px;display:grid;grid-template-columns:107px 110px;row-gap:14.6px;font-size:8.5px}
.foot-links li{list-style:none;padding-left:10px;position:relative}
.foot-links li::before{content:"";position:absolute;left:0;top:3px;width:4px;height:4px;border-radius:50%;background:#fff}
.contact{position:absolute;left:294px;top:77px;font-size:8.5px;line-height:16px}
.contact div{display:flex;gap:10px;margin-bottom:6px}
.contact svg{flex:none;margin-top:2px}
.contact .tel{font-size:11.5px;font-weight:700;color:#fff}
.partner{position:absolute;left:511px;top:44px;font-size:8.5px}
.partner .mark{font-size:20px;color:#fff;font-weight:300}
.partner p{margin-top:8px}
.social{display:flex;gap:9px;margin-top:14px}
.social i{width:16px;height:16px;border-radius:50%;background:#fff}

.bottom-bar{height:54px;position:relative;font-size:8.5px;color:#888}
.pq{position:absolute;left:0;top:14px;width:25px;height:25px;background:#c5d4e3}
.bottom-bar .reg{position:absolute;left:38px;top:22px}
.bottom-bar .copy{position:absolute;right:0;top:22px}
</style>
</head>
<body>

<header class="site-header">
  <div class="wrap">
    <div class="brand">
      <div class="brand-square"></div>
      <div class="brand-name"><small>Gerüstbau</small>Brenner</div>
    </div>
    <nav class="main-nav">
      <span>Startseite</span>
      <span class="active">Leistungen ⌄</span>
      <span>Unternehmen</span>
      <span>Aktuelles</span>
      <span>Karriere</span>
      <span>Impressum</span>
      <span>Datenschutz</span>
    </nav>
    <ul class="dropdown">
      <li>Fassadengerüste</li>
      <li>Gerüste für Kirchen- und<br>Denkmalsanierungen</li>
      <li>Rundrüstungen an Türmen</li>
      <li>Überdachungen mit<br>Kolvex-Kassettendach</li>
      <li>weitere Spezialgrüste</li>
    </ul>
  </div>
</header>

<section class="hero" role="img" aria-label="Foto: Gerüstbauer tragen Gerüstteile auf einem Gerüst vor bewölktem Himmel">
  <div class="hero-cta">
    <h1><b>Wir lösen</b> auch<br>Ihre <b>Gerüstprobleme</b></h1>
    <p>Sprechen Sie mit uns!</p>
    <div class="phone-pill">Tel.: 03761-204417 <span></span></div>
  </div>
</section>

<section class="about">
  <div class="wrap">
    <div class="badge blue">ÜBER UNS</div>
    <h2>ÜBER <em>30 JAHRE</em><span>GERÜSTBAU BRENNER</span></h2>
    <p class="about-text">In der über 20-jährigen erfolgreichen Firmengeschichte waren und sind wir stets ein leistungsstarker und kompetenter Partner für unsere Kunden im Raum Sachsen und Thüringen. Unser Aktionsradius erstreckt sich auf ca. 100 km im Umkreis. Mit unserem im Jahresdurchschnitt 15-köpfigem Team sind wir in der Lage, die meisten im Gerüstbau geforderten Leistungen zu erbringen. Wir arbeiten ständig mit verschiedenen Bau- und Dachdeckerfirmen, Handwerksbetrieben, Ingenieurbüros, Kommunen, Kirchen, landwirtschaftlichen Betrieben, der Industrie und Privatpersonen zusammen. Einen Einblick über von uns ausgeführte Arbeiten erhalten Sie auf der nachfolgenden Seite.</p>
    <div class="btn-outline">Referenzen</div>
    <div class="about-visual" role="img" aria-label="Illustration: freistehendes Gerüst mit Firmenbanner"></div>
  </div>
</section>

<section class="services">
  <div class="wrap">
    <div class="badge green">UNSERE LEISTUNGEN</div>
    <p class="services-intro">Wir arbeiten ausschließlich mit Kolvex-Gerüsten.<br>Dafür stehen uns ca. 40.000 m² Kolvex-Sturm-Gerüst, ca. 4.000 m² Modulgerüst, Kassetten- und Planendächer,<br>Treppenaufgänge und Nottreppen, Fahr- und Rollgerüste sowie weitere Sonderteile zur Verfügung.<br><br>Für den Transport des Gerüstmaterials haben wir vier LKW, z.T. mit Ladekran, und einen<br>Transporter im Einsatz.</p>
    <svg class="arrow" style="left:-49px" width="24" height="34" viewBox="0 0 24 34"><path d="M18 3 5 17l13 14" fill="none" stroke="#2f75ad" stroke-width="5"/></svg>
    <svg class="arrow" style="left:771px" width="24" height="34" viewBox="0 0 24 34"><path d="M6 3l13 14L6 31" fill="none" stroke="#fff" stroke-width="5"/></svg>
    <div class="slider">
      <div class="svc-card"><div class="photo" role="img" aria-label="Foto: eingerüstete historische Fassade" style="background:linear-gradient(180deg,#c9ced4,#6b6458)"></div><h3>FASSADENGERÜSTE</h3></div>
      <div class="svc-card"><div class="photo" role="img" aria-label="Foto: Gebäude mit Kassettendach und Planen" style="background:linear-gradient(180deg,#7fa3d4,#d8dde2 55%,#6b8a55)"></div><h3>KOLVEX-KASSETTENDACH</h3></div>
      <div class="svc-card"><div class="photo" role="img" aria-label="Foto: eingerüsteter Kirchturm mit Kran" style="background:linear-gradient(180deg,#d7dbe0,#9a9280)"></div><h3>RUNDRÜSTUNGEN AN TÜRMEN</h3></div>
    </div>
    <div class="dots"><i></i><i></i><i></i></div>
  </div>
  <div class="services-band"></div>
</section>

<section class="news">
  <div class="wrap">
    <div class="badge blue">AKTUELLES</div>
    <div class="news-grid">
      <article class="news-card">
        <div class="photo" role="img" aria-label="Foto: Schloss mit Gerüst" style="background:linear-gradient(180deg,#8fb0d6,#9a7a62)"></div>
        <div class="body"><h3>Schloss Lichtenstein in Sachsen -<br>Wir bauen das Gerüst!</h3><p>Das Schloss Lichtenstein befindet sich in exponierter Lage auf dem Schlossberg in Lichtenstein und wird derzeit denkmal-schutzgerecht zu einem Schlosshotel mit Wellnesslandschaft umgebaut und saniert.</p><a>mehr erfahren</a></div>
      </article>
      <article class="news-card">
        <div class="photo" role="img" aria-label="Foto: Handwerker mit gelbem Schutzhelm und Werkzeuggürtel" style="background:linear-gradient(180deg,#a06a55,#c9a14a)"></div>
        <div class="body"><h3>Neue engagierte Mitarbeiter<br>für das Jahr 2022 gesucht</h3><p>Sie sind Gerüstbauer oder haben einen an-deren einschlägigen Bauberuf und möchten sich beruflich verändern? Dann rufen Sie bei uns an! Auch Gerüstbauhelfer sind herzlich willkommen, Sie werden hier angelernt.</p><a>mehr erfahren</a></div>
      </article>
      <article class="news-card">
        <div class="photo" role="img" aria-label="Foto: eingerüstetes Gebäude am Hauptmarkt" style="background:linear-gradient(180deg,#5d7fb5,#c4b79a)"></div>
        <div class="body"><h3>Unser letztes Projekt:<br>Auf dem Zwickauer Hauptmarkt</h3><p>Lorem ipsum dolor sit amet, consetetur sadipscing elitr, sed diam nonumy eirmod tempor invidunt ut labore et dolore magna aliquyam erat, sed diam voluptua. At vero eos et accusam et justo duo dolores et...</p><a>mehr erfahren</a></div>
      </article>
    </div>
  </div>
</section>

<footer class="site-footer">
  <div class="wrap">
    <h4 style="left:0">UNSERE GERÜSTE</h4>
    <ul class="foot-links">
      <li>Fassadengerüste</li><li>für Kirchen &amp; Denkmälern</li>
      <li>Kassettendächer</li><li>Fahrgerüste</li>
      <li>Spezialgerüste</li><li>Über uns</li>
      <li>Treppentürme</li><li>Karriere</li>
    </ul>
    <h4 style="left:294px">KONTAKT</h4>
    <div class="contact">
      <div><svg width="10" height="10" viewBox="0 0 10 10"><rect width="10" height="10" rx="2" fill="#fff"/><path d="M3 2.5c0 2.5 2 4.5 4.5 4.5" stroke="#2d2d2d" stroke-width="1.4" fill="none"/></svg><span class="tel">03761-204417</span></div>
      <div><svg width="10" height="10" viewBox="0 0 10 10"><path d="M5 1 0 5h1.5v4h2.5V6.5h2V9h2.5V5H10z" fill="#fff"/></svg><span>Obere Lindenstraße 7<br>08371 Glauchau</span></div>
      <div><svg width="10" height="10" viewBox="0 0 10 10"><circle cx="5" cy="5" r="4" fill="none" stroke="#fff" stroke-width="1.4"/><path d="M5 2.8V5h1.8" stroke="#fff" stroke-width="1.2" fill="none"/></svg><span>Öffnungszeiten: 8:00 - 17:00 Uhr<br>Samstag von 8:00 - 14:0 Uhr</span></div>
    </div>
    <div class="partner">
      <div class="mark">Kolvex</div>
      <p>Wir bauen mir dem Kolvex Gerüst-System</p>
      <p style="margin-top:16px">Datenschutz | Impressum</p>
      <div class="social"><i></i><i></i><i></i></div>
    </div>
  </div>
</footer>

<div class="bottom-bar">
  <div class="wrap">
    <div class="pq"></div>
    <span class="reg">Die Präqualifizierung erfolgte unter der Registriernummer 110.004512</span>
    <span class="copy">© 2022 Gerüstbau Brenner GmbH</span>
  </div>
</div>

</body>
</html>
```